Mockup design for a fashion contest website

The website is a landing page for a fashion contest. Participants are fashion students, designers, merchandisers, stylists, and other fashion enthusiasts. Website should have a clean, modern look and should be "headline-y" in nature. Website should be very visual with good use of images since the audience is fashion (specifically women's clothing). Contestants will earn points by identifying fashion/clothing items within images.

Here's what I am thinking:

Title:
Fashion Contest by Vendrift

Headlines (each with subheadline of 10-15 words )
Can you find the features in the image?
This will be a carousel showing 3-4 images with callouts
Have callouts for each of the categories like this: https://img.examplecdn.test/v/9QwzLm/preview.jpg
Broad categories for items are labeled like:
Top
Dress
Jeans
Pants
Shorts
Blouse
Skirt
Standard
Crop Top
Shirt
Sweater
Detail fashion attributes are in the spreadsheet attached

Earn Points
and see where you stand -- leaderboard graphic
Win Prizes
Need a way to show multiple prizes here:
Grand prizes: Tablo Max, Halvex Lumora QZ-870T Wi-Fi Digital Camera, Stitchwell KR5530TN Sewing Machine, Drafty Linea Max Drawing tablet
Other prizes: Orvane Earlets, Gift cards to great stores: Mivo, Lumo, Blushery, etc.

What You Need To Know
How to Enter (25-30 words)
How do I qualify? (10-15 words)
What are the contest dates (10-15 words)
What is this for? (10-15 words)

----

Tell Your Friends (10 words) [Needs to be shown more prominently as we will have referral bonuses]

The Legal Stuff / Terms & Conditions
[Each subsection 50 words]
Eligibility
Winners & Prizes
Privacy Policy
Judging
Disclaimer

Other sections (shown as links on top perhaps)
Blog - standard blog format. No need for design
Forum - use threadloom software. No need for design
Standings
FAQ
Contact - link to email - no need for design

Need to have clear CTA to sign up on bottom.

Need to Design ‘Standings’ Page:

Show Leaderboard
Ranking, Username, total points, change in ranking (up or down)

Show Total number of images processed. This can be progress bar like in crowdfunding sites:
https://snapbin.test/kTrvo/58ac91d3e0.png
It would say:
300,000 images processed by 1,000 participants
x% of 1,000,000 goal a month left

Goals and Stretch Goals for the Contest

500,000 images
Grand prizes (1 winner)
Other prizes (3 winners)

1,000,000 images
Grand prizes (2 winners)
Other prizes (6 winners)

2,000,000 images
Grand prizes (3 winners)
Other prizes (9 winners)

3,000,000 images
Grand prizes (4 winners)
Other prizes (12 winners)

How to Earn Points

Points awarded for correctly completing task
Points are deducted for making mistakes and unnecessary skips

Help
just a click away. Post a message on the community forum and ask a question.
----
High contrasty (black & white) with one color perhaps blue should be color palette. Look at our logo for design motif ideas.
Updates

Target Market(s)

Fashion community

Industry/Entity Type

Fashion

Number of Pages Required

2 page

Font styles to use
Sans Serif

Requirements
Must have
• one page scroll website (the quiz is a separate page though)
• beautiful graphics and images
• placeholder text where number of words is written
Nice to have
• written copy ideas
Should not have
• the vendrift logo should not be prominently featured. the emphasis is on 'Fashion Contest'

```html
<!DOCTYPE html>
<html lang="en">
<head>
<meta charset="utf-8">
<title>Fashion Contest by Vendrift</title>
<link rel="stylesheet" href="https://fonts.googleapis.com/css2?family=Nunito+Sans:wght@300;400;600;700;800&display=swap">
<style>
:root{
  --ink:#1f1f1f;
  --muted:#8a8a8a;
  --line:#d9d9d9;
  --blue:#1e88d6;
  --blue-deep:#0d4fb8;
  --band-blue:#1d6fd1;
  --grey-band:#ebebeb;
  --footer:#1b1b1b;
  --white:#ffffff;
  --hex-yellow:#f2e012;
  --hex-lime:#7fd321;
  --hex-red:#e8271b;
  --hex-violet:#6a3fc4;
  --hex-cyan:#22a8e2;
  --hex-green:#25b86a;
}
*{box-sizing:border-box;margin:0;padding:0}
html,body{width:1200px;height:4110px;overflow:hidden}
body{font-family:"Nunito Sans",Arial,sans-serif;color:var(--ink);background:var(--white);position:relative}
section,header,footer{position:relative;width:1200px;overflow:hidden}

/* header */
.site-header{height:88px;background:var(--white)}
.brand{position:absolute;left:170px;top:24px;font-size:34px;font-weight:400;letter-spacing:1px;color:var(--ink)}
.main-nav{position:absolute;left:550px;top:35px;display:flex;gap:0}
.main-nav a{font-size:15px;font-weight:600;color:var(--ink);text-decoration:none;text-transform:uppercase;margin-right:52px}
.signup-btn{position:absolute;left:938px;top:24px;width:94px;height:34px;border:2px solid var(--ink);font-size:13px;font-weight:700;display:flex;align-items:center;justify-content:center;text-transform:uppercase}

/* hero */
.hero{height:526px;background:linear-gradient(100deg,#3a3a3a 0%,#7b7b78 35%,#a19f9a 60%,#6c6b68 100%)}
.hero-photo{position:absolute;inset:0}
.hero-copy{position:absolute;left:170px;top:292px;color:var(--white)}
.hero-title{font-size:40px;font-weight:800;line-height:44px;text-transform:uppercase}
.hero-sub{font-size:33px;font-weight:700;line-height:38px;text-transform:uppercase}
.hero-text{font-size:13px;line-height:18px;margin-top:6px;width:400px;opacity:.9}
.hero-dots{position:absolute;left:560px;top:571px;display:flex;gap:8px}
.hero-dots span{width:12px;height:12px;border-radius:50%;background:var(--white)}
.hero-dots span.off{background:transparent;border:2px solid var(--white)}

/* callouts */
.callouts{height:718px;background:var(--white)}
.model{position:absolute;left:384px;top:12px;width:436px;height:674px;background:linear-gradient(180deg,#f3f3f3,#e6e6e6 55%,#f6f6f6)}
.callout-lines{position:absolute;inset:0}
.callout{position:absolute;display:flex;align-items:flex-start;gap:14px}
.callout.left{flex-direction:row-reverse;text-align:right}
.callout h3{font-size:19px;font-weight:700;text-transform:uppercase;line-height:22px;letter-spacing:.3px}
.callout ul{list-style:none;font-size:11px;line-height:17px;margin-top:6px}
.hex{width:44px;height:48px;flex:none;display:flex;align-items:center;justify-content:center;color:var(--white);font-weight:700;font-size:20px;clip-path:polygon(50% 0,100% 25%,100% 75%,50% 100%,0 75%,0 25%)}
.c1{background:var(--hex-yellow)}.c2{background:var(--hex-lime)}.c3{background:var(--hex-red)}
.c4{background:var(--hex-violet)}.c5{background:var(--hex-cyan)}.c6{background:var(--hex-green)}

/* leaderboard */
.standings{height:443px;background:var(--grey-band)}
.section-title{text-align:center;font-weight:600}
.standings .section-title{position:absolute;top:48px;width:100%;font-size:25px}
.board{position:absolute;left:293px;top:112px;width:617px;background:var(--white);border:1px solid var(--line)}
.board-row{height:54px;display:flex;align-items:center;border-bottom:1px solid var(--line);font-size:17px;position:relative}
.board-row:last-child{border-bottom:0}
.rank{position:absolute;left:36px;color:#444}
.player{position:absolute;left:154px;color:var(--blue);font-weight:600}
.pts,.delta{position:absolute;width:38px;height:38px;border-radius:50%;display:flex;align-items:center;justify-content:center;font-size:15px;color:var(--white)}
.pts{left:469px;background:var(--blue)}
.delta{left:518px;background:#c4c4c4}

/* prizes */
.prizes{height:420px;background:linear-gradient(180deg,#1d8ee0 0%,#1560c9 55%,#0c3ea8 100%);color:var(--white)}
.prizes .section-title{position:absolute;top:26px;width:100%;font-size:34px;font-weight:400}
.prize-tabs{position:absolute;left:460px;top:88px;display:flex;gap:8px}
.prize-tabs span{height:34px;padding:0 18px;border-radius:17px;display:flex;align-items:center;font-size:15px}
.prize-tabs .active{background:#111;color:var(--white)}
.prize-tabs .idle{background:rgba(255,255,255,.22)}
.prize{position:absolute;top:148px;width:170px;text-align:center}
.prize-photo{width:166px;height:166px;border-radius:50%;border:4px solid var(--white);margin:0 auto}
.prize p{font-size:14px;line-height:19px;margin-top:20px}

/* need to know */
.need-to-know{height:581px}
.need-to-know .section-title{position:absolute;top:56px;width:100%;font-size:34px;font-weight:400;color:var(--blue)}
.rule{position:absolute;left:570px;top:118px;width:60px;height:3px;background:var(--blue)}
.enter-title{position:absolute;top:140px;width:100%;text-align:center;font-size:30px;font-weight:600}
.enter-text{position:absolute;left:190px;top:188px;width:820px;text-align:center;font-size:12.5px;line-height:21px;color:var(--muted)}
.faq{position:absolute;top:370px;width:270px}
.faq h4{font-size:19px;font-weight:600;margin-bottom:14px}
.faq p{font-size:12.5px;line-height:20px;color:var(--muted)}

/* tell friends */
.tell-friends{height:348px;background:var(--band-blue);color:var(--white);text-align:center}
.chat-icon{position:absolute;left:566px;top:60px}
.tell-friends h2{position:absolute;top:128px;width:100%;font-size:34px;font-weight:400}
.tell-friends p{position:absolute;left:230px;top:178px;width:740px;font-size:18px;line-height:25px}
.click-btn{position:absolute;left:532px;top:248px;width:136px;height:38px;border-radius:19px;background:var(--white);color:var(--band-blue);font-size:16px;font-weight:600;display:flex;align-items:center;justify-content:center}

/* terms */
.terms{height:838px}
.terms .kicker{position:absolute;top:44px;width:100%;text-align:center;font-size:25px}
.terms .kick-rule{position:absolute;left:580px;top:84px;width:40px;height:2px;background:var(--ink)}
.terms h2{position:absolute;top:90px;width:100%;text-align:center;font-size:34px;font-weight:400}
.clause{position:absolute;width:420px}
.clause h3{font-size:22px;font-weight:400;margin-bottom:12px}
.clause p{font-size:12.5px;line-height:21px;color:var(--muted)}
.clause.wide{width:880px}

/* footer */
.site-footer{height:148px;background:var(--footer);color:#ddd;text-align:center}
.site-footer p{position:absolute;top:38px;width:100%;font-size:14px}
.social{position:absolute;left:526px;top:76px;display:flex;gap:8px}
.social span{width:34px;height:34px;border-radius:50%;border:2px solid #ddd}
</style>
</head>
<body>

<header class="site-header">
  <div class="brand">VENDRIFT</div>
  <nav class="main-nav">
    <a href="#">Home</a><a href="#">Blog</a><a href="#">Forum</a><a href="#">Contact</a>
  </nav>
  <div class="signup-btn">Sign Up</div>
</header>

<section class="hero">
  <div class="hero-photo" role="img" aria-label="Fashion model in a denim jacket posing against a concrete wall"></div>
  <div class="hero-copy">
    <h1 class="hero-title">Welcome to Vendrift</h1>
    <div class="hero-sub">Turpis Mauris Neque</div>
    <p class="hero-text">sociosqu ad litora torquent per conubia nostra per inceptos hymenaeos Proin nulla arcu nonummy feriet, dictum</p>
  </div>
  <div class="hero-dots"><span class="off"></span><span></span><span></span><span></span></div>
</section>

<section class="callouts">
  <div class="model" role="img" aria-label="Full-length model in a white shirt and patterned cropped trousers"></div>
  <svg class="callout-lines" width="1200" height="718" aria-hidden="true">
    <g stroke="#cfcfcf" stroke-width="1.5" fill="none">
      <polyline points="340,186 420,130 560,130"/>
      <polyline points="340,318 560,318"/>
      <polyline points="340,438 430,438 520,400"/>
      <polyline points="860,186 780,130 640,130"/>
      <polyline points="860,318 650,318"/>
      <polyline points="860,444 760,444 690,410"/>
    </g>
  </svg>
  <div class="callout left" style="left:160px;top:164px;width:202px">
    <div class="hex c1">1</div>
    <div><h3>Necklines</h3><ul><li>Asymmetric</li><li>Banded</li><li>Cowl</li></ul></div>
  </div>
  <div class="callout left" style="left:160px;top:296px;width:202px">
    <div class="hex c2">2</div>
    <div><h3>Lengths</h3><ul><li>Boy Short</li><li>Regular</li><li>Short</li></ul></div>
  </div>
  <div class="callout left" style="left:160px;top:414px;width:202px">
    <div class="hex c3">3</div>
    <div><h3>Prints</h3><ul><li>Leopard</li><li>Snake</li><li>Alligator</li></ul></div>
  </div>
  <div class="callout" style="left:840px;top:164px">
    <div class="hex c4">4</div>
    <div><h3>Lengths</h3><ul><li>Waist</li><li>Hipbone</li><li>2" below hip</li></ul></div>
  </div>
  <div class="callout" style="left:840px;top:294px">
    <div class="hex c5">5</div>
    <div><h3>Waistlines</h3><ul><li>Empire</li><li>High-waist</li><li>Waist &amp; Hipbone</li></ul></div>
  </div>
  <div class="callout" style="left:840px;top:420px">
    <div class="hex c6">6</div>
    <div><h3>Materials</h3><ul><li>Batiste</li><li>Lace</li><li>Eyelet</li></ul></div>
  </div>
</section>

<section class="standings">
  <h2 class="section-title">Earn Points and See Where You Stand</h2>
  <div class="board">
    <div class="board-row"><span class="rank">01</span><span class="player">Dalen Ashworth</span><span class="pts">08</span><span class="delta">-11</span></div>
    <div class="board-row"><span class="rank">02</span><span class="player">Mirela Voss</span><span class="pts">07</span><span class="delta">-10</span></div>
    <div class="board-row"><span class="rank">03</span><span class="player">Corbin Halley</span><span class="pts">04</span><span class="delta">-05</span></div>
    <div class="board-row"><span class="rank">04</span><span class="player">Teo Ranford</span><span class="pts">02</span><span class="delta">-18</span></div>
    <div class="board-row"><span class="rank">05</span><span class="player">Inara Kestel</span><span class="pts">01</span><span class="delta">-10</span></div>
  </div>
</section>

<section class="prizes">
  <h2 class="section-title">Win Prizes</h2>
  <div class="prize-tabs"><span class="active">Grand Prizes</span><span class="idle">Other Prizes</span></div>
  <div class="prize" style="left:175px"><div class="prize-photo" role="img" aria-label="Tablet with stylus" style="background:radial-gradient(circle,#3a3a3a,#111)"></div><p>Tablo Max</p></div>
  <div class="prize" style="left:351px"><div class="prize-photo" role="img" aria-label="Compact digital camera" style="background:radial-gradient(circle,#6a6a6a,#1a1a1a)"></div><p>Halvex Lumora<br>QZ-870T</p></div>
  <div class="prize" style="left:526px"><div class="prize-photo" role="img" aria-label="Digital camera on a table" style="background:radial-gradient(circle,#c8742c,#3b2a1e)"></div><p>Wi-Fi Digital<br>Camera Stitchwell</p></div>
  <div class="prize" style="left:704px"><div class="prize-photo" role="img" aria-label="Sewing machine" style="background:radial-gradient(circle,#e9efe7,#3c8a6c)"></div><p>KR5530TN<br>Sewing Machine</p></div>
  <div class="prize" style="left:879px"><div class="prize-photo" role="img" aria-label="Drawing tablet with pen" style="background:radial-gradient(circle,#e4e6ea,#6c7480)"></div><p>Drafty Linea Max<br>Drawing tablet</p></div>
</section>

<section class="need-to-know">
  <h2 class="section-title">What You Need To Know</h2>
  <div class="rule"></div>
  <h3 class="enter-title">How to Enter</h3>
  <p class="enter-text">commodo a mi Morbi ornare gravida elit Integer congue augue et malesuada iaculis ipsum dui aliquet felis at cursus magna nisl nec elit Praesent elementum elit at tellus nec ultricies sit amet porttitor mattis enim in massa libero interdum nec interdum vel blandit sed nulla in ullamcorper est eget tempor cursus neque mi i erat fermentum vel congue id euismod in elit Fusce ultriciesviverra in gravida eu mattis in ante Morbi eget arcu Morbi porta libero id ullamcorper nonummy nibh ligula pulvinar metus eget consectetuer</p>
  <div class="faq" style="left:164px"><h4>How do I qualify?</h4><p>commodo a mi Morbi ornare gravida elit Integer congue augue et malesuada iaculis ipsum dui aliquet felis at cursus magna nisl nec elit Praesent elementum</p></div>
  <div class="faq" style="left:466px"><h4>What are the contest dates</h4><p>commodo a mi Morbi ornare gravida elit Integer congue augue et malesuada iaculis ipsum dui aliquet felis at cursus magna nisl nec elit Praesent elementum</p></div>
  <div class="faq" style="left:775px"><h4>What is this for?</h4><p>commodo a mi Morbi ornare gravida elit Integer congue augue et malesuada iaculis ipsum dui aliquet felis at cursus magna nisl nec elit Praesent elementum</p></div>
</section>

<section class="tell-friends">
  <svg class="chat-icon" width="68" height="56" viewBox="0 0 68 56" aria-hidden="true">
    <path d="M34 4C17 4 4 13 4 25c0 6 3 11 9 15l-3 12 13-8c3 1 7 1 11 1 17 0 30-9 30-20S51 4 34 4z" fill="none" stroke="#fff" stroke-width="3"/>
    <g stroke="#fff" stroke-width="3" stroke-linecap="round"><line x1="22" y1="18" x2="46" y2="18"/><line x1="22" y1="26" x2="46" y2="26"/><line x1="22" y1="34" x2="38" y2="34"/></g>
  </svg>
  <h2>Tell Your Friends</h2>
  <p>Praesent elementum elit at tellus nec ultricies sit amet porttitor mattis enim In massa libero interdum nec interdum vel blandit sed nulla In ullamcorper</p>
  <div class="click-btn">Click here</div>
</section>

<section class="terms">
  <div class="kicker">The Legal Stuff</div>
  <div class="kick-rule"></div>
  <h2>Terms &amp; Conditions</h2>
  <div class="clause" style="left:164px;top:184px"><h3>1. Eligibility</h3><p>commodo a mi Morbi ornare gravida elit Integer congue augue et malesuada iaculis ipsum dui aliquet felis at cursus magna nisl nec elit Praesent elementum elit at tellus nec ultricies sit amet porttitor mattis enim In massa libero interdum nec interdum vel blandit sed nulla In ullamcorper est eget tempor cursus neque mi</p></div>
  <div class="clause" style="left:622px;top:184px"><h3>2. Winners &amp; Prizes</h3><p>commodo a mi Morbi ornare gravida elit Integer congue augue et malesuada iaculis ipsum dui aliquet felis at cursus magna nisl nec elit Praesent elementum elit at tellus nec ultricies sit amet porttitor mattis enim In massa libero interdum nec interdum vel blandit sed nulla In ullamcorper est eget tempor cursus neque mi</p></div>
  <div class="clause" style="left:164px;top:400px"><h3>3. Privacy Policy</h3><p>commodo a mi Morbi ornare gravida elit Integer congue augue et malesuada iaculis ipsum dui aliquet felis at cursus magna nisl nec elit Praesent elementum elit at tellus nec ultricies sit amet porttitor mattis enim In massa libero interdum nec interdum vel blandit sed nulla In ullamcorper est eget tempor cursus neque mi i erat fermentum vel congue id euismod in elit Fusce ultricie</p></div>
  <div class="clause" style="left:622px;top:400px"><h3>4. Judging</h3><p>commodo a mi Morbi ornare gravida elit Integer congue augue et malesuada iaculis ipsum dui aliquet felis at cursus magna nisl nec elit Praesent elementum elit at tellus nec ultricies sit amet porttitor mattis enim In massa libero interdum nec interdum vel blandit sed nulla In ullamcorper est eget tempor cursus neque mi i erat fermentum vel congue id euismod in elit Fusce ultricie</p></div>
  <div class="clause wide" style="left:164px;top:616px"><h3>5. Disclaimer</h3><p>commodo a mi Morbi ornare gravida elit Integer congue augue et malesuada iaculis ipsum dui aliquet felis at cursus magna nisl nec elit Praesent elementum elit at tellus nec ultricies sit amet porttitor mattis enim In massa libero interdum nec interdum vel blandit sed nulla In ullamcorper est eget tempor cursus neque mi i erat fermentum vel congue id euismod in elit Fusce ultriciesviverra in gravida eu mattis in ante Morbi eget arcu Morbi porta libero id ullamcorper nonummy nibh ligula pulvinar metus eget dui non lacus Ut ac mi quis lacus mollis aliquam Curabitur iaculis tempus eros Curabitur vel mi sit amet magna malesuada ultrices Ut nisi erat fe</p></div>
</section>

<footer class="site-footer">
  <p>© 2017 Company Name &nbsp;All right reserved &nbsp;Term of Use</p>
  <div class="social" aria-label="Social links"><span></span><span></span><span></span><span></span></div>
</footer>

</body>
</html>
```